Velvet Heel Ball Poster

We need a poster design for a local event we are holding in our town. The band playing is called "Tinsel" and the theme is "Glam Rock". We would like to see a design that ties in with the Glam Rock theme and it should be very eyecatching. I have attached a file showing the type of look that you might think is suitable but I am open to suggestions! Thanks so much - I am looking forward to seeing your ideas!!

It also needs to say on the poster that the event is sponsored by the Wandoora CRC (see attached logo) and the Wandoora Progress Association (see attached logo)

Industry/Entity Type

Town

Requirements
Must have
• Must have the following wording...

Calling all Rockers...
The Wandoora Progress Association proudly presents live music by
"Tinsel"
Friday 26th October
7:30pm
Wandoora Hall
Tickets $20 - Available from the Wandoora CRC
Dress - GLAM ROCK

```html
<!DOCTYPE html>
<html lang="en">
<head>
<meta charset="utf-8">
<title>Velvet Heel Ball – Tinsel Live</title>
<link rel="stylesheet" href="https://fonts.googleapis.com/css2?family=Russo+One&family=Bungee&family=Bungee+Inline&family=Anton&family=Archivo+Black&family=EB+Garamond:wght@500;600&family=Tinos:wght@700&display=swap">
<style>
  :root {
    --black: #050505;
    --white: #ffffff;
    --ink: #1c1c1c;
    --magenta: #e0197f;
    --yellow: #f4c430;
    --blue: #3a4fd8;
    --purple: #a81fc8;
    --stage: #3a3a3e;
    --red-top: #ff5a4a;
    --red-bottom: #8c0a12;
    --panel: rgba(205, 205, 210, 0.55);
  }
  * { margin: 0; padding: 0; box-sizing: border-box; }
  html, body { width: 800px; height: 1200px; overflow: hidden; background: var(--black); }
  .poster {
    position: relative; width: 800px; height: 1200px; overflow: hidden;
    background: var(--black); color: var(--white);
  }
  .stage-scene {
    position: absolute; inset: 0;
    background:
      radial-gradient(ellipse 150px 420px at 150px 420px, rgba(224,25,127,.75), transparent 70%),
      radial-gradient(ellipse 150px 420px at 650px 420px, rgba(224,25,127,.75), transparent 70%),
      radial-gradient(ellipse 90px 300px at 330px 330px, rgba(244,196,48,.7), transparent 70%),
      radial-gradient(ellipse 90px 300px at 470px 330px, rgba(244,196,48,.6), transparent 70%),
      radial-gradient(ellipse 70px 200px at 400px 300px, rgba(58,79,216,.9), transparent 70%),
      radial-gradient(ellipse 260px 180px at 400px 560px, rgba(255,255,255,.75), transparent 70%),
      radial-gradient(ellipse 240px 150px at 400px 800px, rgba(168,31,200,.7), transparent 70%),
      radial-gradient(ellipse 170px 200px at 60px 1010px, rgba(255,255,255,.9), transparent 70%),
      radial-gradient(ellipse 200px 240px at 740px 1020px, rgba(255,255,255,.95), transparent 70%),
      radial-gradient(ellipse 130px 300px at 60px 560px, rgba(244,196,48,.55), transparent 70%),
      radial-gradient(ellipse 130px 300px at 740px 560px, rgba(244,196,48,.55), transparent 70%),
      linear-gradient(180deg, var(--black) 0 200px, #2a1a2a 300px, var(--stage) 640px, #2b2b2e 1000px, var(--black) 1200px);
  }
  .band-silhouette {
    position: absolute; left: 233px; top: 380px; width: 307px; height: 153px;
    background: linear-gradient(180deg, rgba(30,30,34,.75), rgba(30,30,34,.35));
    border-radius: 40px 40px 6px 6px;
  }
  .calling-all {
    position: absolute; top: -22px; left: 0; width: 100%; text-align: center;
    font-family: "Russo One", sans-serif; font-size: 88px; letter-spacing: 4px;
    filter: blur(2.5px);
  }
  .presenter {
    position: absolute; top: 108px; left: 0; width: 100%; text-align: center;
    white-space: nowrap;
    font-family: "Russo One", sans-serif; font-style: italic; font-weight: 400; font-size: 33px;
    letter-spacing: 0; -webkit-text-stroke: 1px var(--black);
    text-shadow: 2px 2px 0 #555;
  }
  .presents {
    position: absolute; top: 158px; left: 0; width: 100%; text-align: center;
    font-family: "Bungee", sans-serif; font-size: 50px; letter-spacing: 1px;
    color: var(--white); -webkit-text-stroke: 2px var(--black);
  }
  .band-name {
    position: absolute; top: 236px; left: 0; width: 100%; text-align: center;
    font-family: "Russo One", sans-serif; font-weight: 400; font-size: 72px; letter-spacing: 8px;
    line-height: 1;
    background: linear-gradient(180deg, var(--red-top), var(--red-bottom));
    -webkit-background-clip: text; background-clip: text; color: transparent;
  }
  .live {
    position: absolute; top: 314px; left: 0; width: 100%; text-align: center;
    font-family: "Tinos", serif; font-weight: 700; font-size: 46px;
  }
  .side-call {
    position: absolute; top: 395px; writing-mode: vertical-rl;
    font-family: "Bungee Inline", sans-serif; font-size: 66px; letter-spacing: 2px;
    color: var(--white); text-shadow: 0 0 10px rgba(244,196,48,.9);
  }
  .side-call--left { left: 2px; }
  .side-call--right { right: 2px; }
  .event-details {
    position: absolute; left: 537px; top: 487px; width: 163px; height: 250px;
    background: var(--panel); color: var(--ink); text-align: center;
    font-family: "EB Garamond", serif; font-weight: 500; font-size: 27px; line-height: 1.2;
    padding-top: 20px;
  }
  .theme {
    position: absolute; left: 0; top: 665px; width: 100%; text-align: center;
    font-family: "Anton", sans-serif; color: var(--white); line-height: .95;
    transform: perspective(700px) rotateX(25deg) rotate(5deg) translateX(30px);
    text-shadow: 0 0 6px rgba(0,0,0,.4);
  }
  .theme-line { display: block; }
  .theme-line--glam { font-size: 92px; letter-spacing: 4px; margin-right: 60px; }
  .theme-line--rock { font-size: 170px; letter-spacing: 14px; }
  .tickets {
    position: absolute; left: 14px; top: 1040px;
    font-family: "EB Garamond", serif; line-height: 1.25;
  }
  .tickets-price { font-size: 46px; font-weight: 500; }
  .tickets-source, .dress-code { font-size: 26px; }
  .sponsors {
    position: absolute; left: 386px; top: 1022px; width: 360px;
  }
  .sponsors-title {
    font-family: "Archivo Black", sans-serif; font-size: 34px; margin-left: 6px;
  }
  .sponsor-logo {
    position: absolute; background: var(--white); color: var(--ink);
    font-family: "Archivo Black", sans-serif; text-align: center;
    display: flex; align-items: center; justify-content: center; gap: 6px;
  }
  .sponsor-logo--crc { left: 5px; top: 55px; width: 189px; height: 103px; font-size: 16px; line-height: 1.15; padding: 8px; }
  .sponsor-logo--town { left: 245px; top: 62px; width: 98px; height: 92px; font-size: 14px; flex-direction: column; }
  .logo-square { width: 34px; height: 34px; background: #9a9a9a; }
</style>
</head>
<body>
<main class="poster">
  <div class="stage-scene" role="img" aria-label="Stage lit by pink, yellow and blue spotlights with a purple paint splash on the floor"></div>
  <div class="band-silhouette" role="img" aria-label="Silhouettes of four band members playing guitars"></div>

  <div class="calling-all">ALL</div>
  <h2 class="presenter">WANDOORA PROGRESS ASSOCIATION</h2>
  <div class="presents">PRESENTS</div>
  <h1 class="band-name">TINSEL</h1>
  <div class="live">Live</div>

  <div class="side-call side-call--left">CALLING</div>
  <div class="side-call side-call--right">ROCKERS</div>

  <div class="event-details">
    Friday<br>October 26<br>7:30 pm<br>@<br>Wandoora<br>Hall
  </div>

  <div class="theme">
    <span class="theme-line theme-line--glam">GLAM</span>
    <span class="theme-line theme-line--rock">ROCK</span>
  </div>

  <div class="tickets">
    <div class="tickets-price">Tickets:$20</div>
    <div class="tickets-source">provided by the wandoora CRC</div>
    <div class="dress-code">Dress: Glam Rock</div>
  </div>

  <section class="sponsors">
    <div class="sponsors-title">sponsers</div>
    <div class="sponsor-logo sponsor-logo--crc">Wandoora Community Resource Centre</div>
    <div class="sponsor-logo sponsor-logo--town"><span class="logo-square"></span>WANDOORA</div>
  </section>
</main>
</body>
</html>
```